Thistlecrest Superfoods Packaging Design

We are looking for a design for our premium superfoods powders and blends. Packaging dimensions are 21cm x 13cm Kraft packaging (light brown background). This design should be a blueprint for other products that we will be marketing including lions mane mushroom, reishi mushroom, Chaga mushroom, Spirilina, bee pollen, açai powder and the like. The design should be clean but earthy, and the template replicable for other products.

```html
<!DOCTYPE html>
<html lang="en">
<head>
<meta charset="utf-8">
<title>Thistlecrest Superfoods – Reishi Mushroom</title>
<link rel="stylesheet" href="https://fonts.googleapis.com/css2?family=Raleway:wght@300;400;500&family=Libre+Baskerville:ital@1&display=swap">
<style>
  :root {
    --mint: #c3e4dc;
    --ink: #333333;
    --ink-soft: #4a4a4a;
    --etch-dark: #2b2b2b;
    --etch-mid: #8d9a96;
    --badge-green: #6aa84f;
    --badge-dark: #3f6b35;
    --band-white: #ffffff;
    --band-orange: #e8a35c;
  }
  html, body {
    margin: 0;
    padding: 0;
    overflow: hidden;
  }
  .pack {
    position: relative;
    width: 744px;
    height: 1200px;
    background: var(--mint);
    overflow: hidden;
    color: var(--ink);
    font-family: "Raleway", sans-serif;
  }
  .mushroom-art {
    position: absolute;
    border-radius: 50%;
  }
  .mushroom-art--left {
    left: -70px;
    top: -60px;
    width: 400px;
    height: 340px;
    background: radial-gradient(ellipse at 55% 45%, var(--etch-mid) 0%, var(--etch-dark) 70%, var(--mint) 72%);
  }
  .mushroom-art--right {
    right: -40px;
    top: -30px;
    width: 330px;
    height: 300px;
    background: radial-gradient(ellipse at 45% 50%, var(--etch-mid) 0%, var(--etch-dark) 68%, var(--mint) 70%);
  }
  .brand {
    position: absolute;
    left: 420px;
    top: 420px;
    width: 220px;
    text-align: center;
    font-family: "Raleway", sans-serif;
    font-weight: 400;
    font-size: 22px;
    line-height: 1.3;
    letter-spacing: 1px;
    color: var(--ink);
  }
  .product-title {
    position: absolute;
    left: 42px;
    top: 556px;
    margin: 0;
    font-family: "Raleway", sans-serif;
    font-weight: 300;
    font-size: 58px;
    line-height: 64px;
    letter-spacing: 1px;
    color: var(--ink);
  }
  .intro {
    position: absolute;
    left: 42px;
    top: 718px;
    width: 335px;
    margin: 0;
    font-size: 14px;
    line-height: 19px;
    font-weight: 400;
    text-transform: uppercase;
    color: var(--ink-soft);
    letter-spacing: 0.3px;
  }
  .nutrient-list {
    position: absolute;
    left: 42px;
    top: 870px;
    margin: 0;
    padding: 0;
    list-style: none;
  }
  .nutrient {
    display: flex;
    align-items: center;
    height: 52px;
  }
  .nutrient__factor {
    width: 62px;
    font-size: 36px;
    font-weight: 400;
    color: var(--ink);
  }
  .nutrient__label {
    font-size: 11px;
    line-height: 14px;
    font-weight: 500;
    text-transform: uppercase;
    color: var(--ink-soft);
  }
  .benefits {
    position: absolute;
    left: 412px;
    top: 716px;
    width: 292px;
    margin: 0;
    font-family: "Libre Baskerville", serif;
    font-style: italic;
    font-size: 13.5px;
    line-height: 21px;
    color: var(--ink);
  }
  .badges {
    position: absolute;
    left: 42px;
    top: 1108px;
    display: flex;
    gap: 14px;
    align-items: center;
  }
  .badge {
    width: 46px;
    height: 46px;
    border-radius: 50%;
    background: var(--badge-green);
  }
  .badge--square {
    width: 62px;
    border-radius: 4px;
    background: var(--badge-dark);
  }
  .net-weight {
    position: absolute;
    right: 40px;
    top: 1122px;
    font-size: 22px;
    font-weight: 400;
    color: var(--ink);
  }
  .base-band {
    position: absolute;
    left: 0;
    bottom: 0;
    width: 744px;
    height: 22px;
    background: var(--band-white);
    border-top: 4px solid var(--band-orange);
  }
</style>
</head>
<body>
<div class="pack">
  <div class="mushroom-art mushroom-art--left" role="img" aria-label="Engraved illustration of a reishi mushroom cap"></div>
  <div class="mushroom-art mushroom-art--right" role="img" aria-label="Engraved illustration of a reishi mushroom cap"></div>

  <div class="brand">Thistlecrest<br>Superfoods</div>

  <h1 class="product-title">REISHI<br>MUSHROOM</h1>

  <p class="intro">Moringa, also known as 'the miracle tree', has been praised for it's health benefits for thousands of years. It is extremely rich in healthy antioxidants and bioactive compounds. In fact it has:</p>

  <ul class="nutrient-list">
    <li class="nutrient"><span class="nutrient__factor">7x</span><span class="nutrient__label">The vitamin C<br>of oranges</span></li>
    <li class="nutrient"><span class="nutrient__factor">4x</span><span class="nutrient__label">The calcium<br>of milk</span></li>
    <li class="nutrient"><span class="nutrient__factor">3x</span><span class="nutrient__label">The potassium<br>of bananas</span></li>
    <li class="nutrient"><span class="nutrient__factor">3x</span><span class="nutrient__label">Iron<br>of spinach</span></li>
  </ul>

  <p class="benefits">The leaves contain all nine essential amino acids and traditionally used in assisting the healing of many ailments. The nutritional diversity is also known to reduce both cholesterol and blood sugar levels whilst and have serious anti-inflammatory benefits. Our 100% organic moringa is grown and harvested in it's native enviornment, supporting premium superfood nutrition.</p>

  <div class="badges">
    <span class="badge"></span>
    <span class="badge"></span>
    <span class="badge badge--square"></span>
    <span class="badge"></span>
  </div>

  <div class="net-weight">250g</div>

  <div class="base-band"></div>
</div>
</body>
</html>
```